Fernbrook Pet Showcase Ticket Card Design

We’re looking to create a complimentary “ticket” card for Fernbrook Pet Showcase that can be handed out physically. We host an event for cat lovers. The card should feel special and collectible. Size will be a standard business card (3.5" x 2") Orientation is open to designer recommendation. This ticket will be used as a complimentary entry pass for select guests, partners, & giveaways. Key elements to Include are the Fernbrook Pet Showcase logo (provided), the words “Complimentary Ticket” or similar wording (open to creative phrasing and cat puns) A blank space for the Event date (to be written in) & Ticket number (to be written in) . Event Name is always "Fernbrook Pet Bazaar & Rehoming Day". We want the ticket to feel clean & modern but slightly playful with a cat-inspired touch (think clever, not kitschy). Could include a subtle cat motif or texture (e.g., whisker lines, paw detail, soft patterning) Open to unique layout ideas that still leave clear writing space. Avoid overcrowding of elements. Ticket should also have fine print "This ticket is not redeemable for cash and cannot be combined with any other offers or discounts, can only be used for the date indicated"

Target Market(s)

Women

Industry/Entity Type

pets

Colors
6B429C
8869AF
B7A5CE
E3DAEB
F3F0F8

Requirements
Must have
• Fernbrook Pet Showcase Logo & words around complimentary ticket as well as the fine print
Nice to have
• cat-inspired touch (think clever, not kitschy). Could include a subtle cat motif or texture (e.g., whisker lines, paw detail, soft patterning)
Should not have
• should not look cartoony

```html
<!DOCTYPE html>
<html lang="en">
<head>
<meta charset="utf-8">
<title>Fernbrook Pet Showcase – Guest Ticket</title>
<link rel="stylesheet" href="https://fonts.googleapis.com/css2?family=Montserrat:wght@400;600&family=Dancing+Script:wght@600&display=swap">
<style>
  :root {
    --page-bg: #e8e9eb;
    --card-bg: #23283b;
    --peach: #f4d5c2;
    --peach-soft: rgba(244, 213, 194, 0.14);
    --paw-tone: rgba(150, 140, 160, 0.35);
    --text-light: #e6e4ec;
    --rule: rgba(230, 228, 236, 0.85);
    --divider-start: rgba(244, 213, 194, 0.1);
    --divider-end: rgba(244, 213, 194, 0.75);
  }
  * { margin: 0; padding: 0; box-sizing: border-box; }
  html, body {
    width: 1147px;
    height: 1200px;
    overflow: hidden;
    background: var(--page-bg);
  }
  .ticket-card {
    position: absolute;
    left: 73px;
    top: 314px;
    width: 1000px;
    height: 572px;
    background: var(--card-bg);
    color: var(--peach);
    font-family: "Montserrat", sans-serif;
    overflow: hidden;
  }
  .brand-name {
    position: absolute;
    left: 60px;
    top: 110px;
    width: 210px;
    font-weight: 600;
    font-size: 30px;
    line-height: 1.12;
    letter-spacing: 0.5px;
  }
  .brand-underline {
    position: absolute;
    left: 60px;
    top: 228px;
    width: 190px;
    height: 1px;
    background: linear-gradient(90deg, var(--divider-start), var(--divider-end));
  }
  .event-name {
    position: absolute;
    left: 320px;
    top: 100px;
    font-size: 26px;
    line-height: 1.25;
    font-weight: 400;
    letter-spacing: 0.6px;
  }
  .header-divider {
    position: absolute;
    left: 310px;
    top: 180px;
    width: 640px;
    height: 1px;
    background: linear-gradient(90deg, var(--divider-start), var(--divider-end));
  }
  .cat-motif {
    position: absolute;
    left: 770px;
    top: 40px;
    width: 170px;
    height: 120px;
    border-radius: 14px;
    background: var(--peach-soft);
  }
  .cat-motif--faint {
    left: 50px;
    top: 490px;
    width: 130px;
    height: 60px;
    background: rgba(150, 140, 160, 0.12);
  }
  .paw-mark {
    position: absolute;
    width: 60px;
    height: 54px;
    border-radius: 50%;
    background: var(--paw-tone);
  }
  .ticket-title {
    position: absolute;
    left: 290px;
    right: 110px;
    top: 200px;
    text-align: center;
    font-family: "Dancing Script", cursive;
    font-size: 78px;
    line-height: 1.1;
    font-weight: 600;
  }
  .write-in {
    position: absolute;
    left: 215px;
    display: flex;
    align-items: flex-end;
    gap: 16px;
    color: var(--text-light);
    font-size: 28px;
    letter-spacing: 0.4px;
  }
  .write-in--date { top: 345px; width: 620px; }
  .write-in--number { top: 405px; width: 640px; }
  .write-in__line {
    flex: 1;
    height: 1px;
    margin-bottom: 8px;
    background: var(--rule);
  }
  .fine-print {
    position: absolute;
    left: 200px;
    width: 720px;
    top: 480px;
    text-align: center;
    font-size: 16px;
    line-height: 1.4;
    color: var(--text-light);
    letter-spacing: 0.3px;
  }
</style>
</head>
<body>
  <main class="ticket-card">
    <div class="brand-name">Fernbrook Pet Showcase</div>
    <div class="brand-underline"></div>

    <p class="event-name">Fernbrook Pet Bazaar<br>&amp; Rehoming Day</p>
    <div class="header-divider"></div>

    <div class="cat-motif" role="img" aria-label="Line drawing of cat ears, nose and whiskers"></div>
    <div class="cat-motif cat-motif--faint" role="img" aria-label="Faint cat ears and whiskers motif"></div>

    <div class="paw-mark" style="left:905px; top:200px;" role="img" aria-label="Faint paw print"></div>
    <div class="paw-mark" style="left:915px; top:275px;" role="img" aria-label="Faint paw print"></div>
    <div class="paw-mark" style="left:910px; top:360px;" role="img" aria-label="Faint paw print"></div>
    <div class="paw-mark" style="left:45px; top:280px;" role="img" aria-label="Faint paw print"></div>
    <div class="paw-mark" style="left:120px; top:345px;" role="img" aria-label="Faint paw print"></div>
    <div class="paw-mark" style="left:60px; top:415px;" role="img" aria-label="Faint paw print"></div>

    <h1 class="ticket-title">Meow Guest Ticket</h1>

    <div class="write-in write-in--date">
      <span class="write-in__label">Event Date:</span>
      <span class="write-in__line"></span>
    </div>
    <div class="write-in write-in--number">
      <span class="write-in__label">Ticket No :</span>
      <span class="write-in__line"></span>
    </div>

    <p class="fine-print">This ticket is not redeemable for cash and cannot be combined with any<br>other offers or discounts, can only be used for the date indicated</p>
  </main>
</body>
</html>
```